Need a redesign for our Wordpress Credit report website

Hi, We need someone to redesign our Wordpress credit report website, brightledgerview.co.za. The designer will be responsible for the following pages:
- home page
- blog page
- single post
- dashboard
- credit report page

About BrightLedgerView.co.za
Bright Ledger View is a consumer focussed credit report platform where South African citizens can get an easy to understand credit report that shows them where to improve their credit scores.

```html
<!DOCTYPE html>
<html lang="en">
<head>
<meta charset="utf-8">
<title>Bright Ledger View – Check your credit score</title>
<link href="https://fonts.googleapis.com/css2?family=Poppins:wght@300;400;500;600;700&display=swap" rel="stylesheet">
<style>
:root{
  --blue:#1e6cc4;
  --blue-dark:#1a5aa8;
  --green:#7dc242;
  --ink:#1d1d1f;
  --text:#3f3f46;
  --muted:#8a8f99;
  --line:#d6dbe3;
  --light:#eef4fc;
  --card:#ffffff;
  --star:#f5b81b;
}
*{box-sizing:border-box;margin:0;padding:0}
html,body{width:1200px;height:4669px;overflow:hidden;background:#fff}
body{font-family:'Poppins',sans-serif;color:var(--ink)}
.page{position:relative;width:1200px;height:4669px;overflow:hidden;background:#fff}
.abs{position:absolute}
.bg{position:absolute;left:0;width:1200px}
.wave{position:absolute;left:0;width:1200px}
.ph{background:linear-gradient(135deg,#cfdcec,#9fb6d3)}

/* header */
.brand{position:absolute;display:flex;align-items:center;gap:10px;font-size:22px;font-weight:500;color:var(--blue)}
.brand-dot{width:34px;height:34px;border-radius:50%;background:var(--green)}
.nav a{position:absolute;top:42px;font-size:14px;color:var(--ink);text-decoration:none}
.nav a.active{color:var(--green)}
.nav a.active::after{content:"";position:absolute;left:4px;right:4px;bottom:-9px;height:2px;background:var(--green)}
.login{position:absolute;left:923px;top:29px;width:145px;height:44px;border:2px solid var(--green);border-radius:22px;color:var(--green);font-size:15px;font-weight:500;display:flex;align-items:center;justify-content:center}

/* hero */
.hero-title{left:160px;top:228px;font-size:38px;line-height:52px;font-weight:700;text-transform:uppercase}
.hero-sub{left:165px;top:334px;width:420px;font-size:14px;line-height:21px;color:var(--text)}
.form-card{left:754px;top:127px;width:319px;height:442px;background:#fff;box-shadow:0 6px 24px rgba(30,60,110,.16)}
.form-title{position:absolute;left:26px;top:24px;font-size:27px;font-weight:700;color:var(--blue);text-transform:uppercase}
.form-title::after{content:"";position:absolute;left:0;right:0;bottom:-4px;height:2px;background:var(--blue)}
.field{position:absolute;left:37px;width:233px;height:45px;border:1.5px solid #9aa3ae;border-radius:5px;font-size:12px;color:var(--muted);padding:14px 18px}
.agree{position:absolute;left:37px;top:349px;font-size:10.5px;color:var(--muted);display:flex;align-items:center;gap:6px}
.agree i{width:13px;height:13px;border:1px solid #777;display:inline-block}
.btn-green{position:absolute;left:73px;top:381px;width:136px;height:41px;background:var(--green);color:#fff;font-weight:600;font-size:15px;display:flex;align-items:center;justify-content:center}

/* headings */
.h2{position:absolute;left:0;width:1200px;text-align:center;font-weight:700;text-transform:uppercase;font-size:38px}

/* about */
.about-title{left:660px;top:812px;font-size:38px;font-weight:700}
.about-text{left:660px;top:870px;width:390px;font-size:13.5px;line-height:20.8px;color:var(--text)}
.about-text b{color:var(--ink);font-weight:600}
.btn-blue{position:absolute;left:660px;top:1080px;width:152px;height:46px;background:var(--blue);border-radius:23px;color:#fff;font-size:15px;font-weight:500;display:flex;align-items:center;justify-content:center}

/* features */
.feat-desc{left:270px;top:1476px;width:660px;text-align:center;font-size:16.5px;line-height:21px;color:var(--text)}
.feat{position:absolute;font-size:19px;font-weight:300;color:#6b6f76;text-align:center;line-height:22px}

/* testimonials */
.tcard{position:absolute;top:2373px;width:469px;height:239px;background:#fff;box-shadow:0 4px 18px rgba(30,60,110,.12);overflow:hidden}
.avatar{position:absolute;border-radius:50%;border:3px solid #fff;box-shadow:0 0 0 2px var(--blue)}
.stars{color:var(--star);letter-spacing:3px;font-size:16px}
.tcard .meta{position:absolute;left:24px;top:58px;display:flex;align-items:center;gap:8px}
.tcard .date{font-size:12px;color:var(--blue);font-weight:500}
.tcard .quote{position:absolute;right:22px;top:16px;font-size:58px;line-height:58px;font-weight:700;color:var(--blue)}
.tcard p{position:absolute;left:24px;top:92px;width:420px;font-size:13px;line-height:21px;color:var(--text)}
.tcard .name{position:absolute;left:24px;top:178px;font-size:12.5px;font-weight:600;color:var(--blue)}
.tcard .role{position:absolute;left:24px;top:198px;font-size:11px;color:var(--muted)}
.arrow{position:absolute;top:2484px;width:26px;height:26px}

/* reviews */
.rcard{position:absolute;width:281px;background:#fff;box-shadow:0 4px 18px rgba(30,60,110,.12);text-align:center}
.rcard .avatar{left:88px;top:-52px;width:104px;height:104px}
.rcard h3{margin-top:78px;font-size:22px;font-weight:500}
.rcard p{margin:14px auto 0;width:230px;font-size:12px;line-height:25px;color:var(--text)}
.rcard .stars{margin-top:8px;font-size:22px}

/* accordion */
.acc{position:absolute;left:207px;width:796px;border:1.5px solid var(--line);font-size:17px;color:var(--ink)}
.acc .q{position:absolute;left:18px;top:18px}
.acc .pm{position:absolute;right:18px;top:12px;font-size:26px;font-weight:300;color:#888}
.acc.open{border:2px solid var(--blue)}
.acc.open .pm{color:var(--blue)}
.acc .a{position:absolute;left:18px;top:64px;width:740px;font-size:13px;line-height:24px;color:var(--text)}

/* payments */
.pay{position:absolute;top:3969px;width:202px;height:202px;border-radius:50%;border:2px solid var(--green);background:#fff;display:flex;align-items:center;justify-content:center;font-size:19px;font-weight:600;color:var(--ink)}
.pay.blue{border-color:var(--blue)}

/* footer */
.social{position:absolute;top:4488px;width:30px;height:30px;border-radius:50%;background:var(--blue)}
.fcol{position:absolute;top:4398px;padding-left:20px;border-left:2px solid var(--green);height:140px}
.fcol h4{font-size:14px;font-weight:600;text-transform:uppercase;margin-top:8px}
.fcol h4.sm{font-size:12.5px}
.fcol ul{list-style:none;margin-top:20px}
.fcol li{font-size:12.5px;line-height:29px;color:var(--text);text-transform:uppercase}
.cinfo{position:absolute;left:872px;display:flex;align-items:center;gap:14px;font-size:10px;line-height:13px;color:var(--text)}
.cinfo .ic{width:30px;height:30px;border-radius:50%;background:var(--green);display:flex;align-items:center;justify-content:center;flex:none}
.copy{position:absolute;left:0;top:4634px;width:1200px;text-align:center;font-size:10.5px;color:var(--muted)}
</style>
</head>
<body>
<div class="page">

  <svg class="bg" style="top:0" width="1200" height="660" viewBox="0 0 1200 660">
    <defs>
      <linearGradient id="heroTint" x1="0" y1="0" x2="1" y2="1">
        <stop offset="0" stop-color="#e4edf9"/><stop offset="1" stop-color="#f5f8fd"/>
      </linearGradient>
      <linearGradient id="band" x1="0" y1="0" x2="1" y2="0">
        <stop offset="0" stop-color="#1e6cc4"/><stop offset=".5" stop-color="#3f8fa0"/><stop offset="1" stop-color="#7dc242"/>
      </linearGradient>
      <linearGradient id="bandR" x1="0" y1="0" x2="1" y2="0">
        <stop offset="0" stop-color="#7dc242"/><stop offset=".5" stop-color="#3f8fa0"/><stop offset="1" stop-color="#1e6cc4"/>
      </linearGradient>
    </defs>
    <path d="M0 0H1200V580C1000 660 820 660 600 622C400 588 200 565 0 640Z" fill="url(#heroTint)"/>
    <path d="M0 628C200 540 400 560 610 598C820 636 1000 650 1200 566V574C1000 666 820 666 600 632C400 598 200 575 0 642Z" fill="url(#band)"/>
  </svg>

  <svg class="wave" style="top:1260px" width="1200" height="960" viewBox="0 0 1200 960">
    <path d="M0 40C250 -10 450 30 650 90C850 150 1000 110 1200 40V830C1000 770 800 800 600 840C400 880 200 860 0 930Z" fill="#f2f6fc"/>
    <path d="M0 48C250 -8 450 30 650 92C850 154 1020 120 1200 30V52C1020 150 850 178 640 116C440 56 250 20 0 58Z" fill="url(#bandR)"/>
    <path d="M0 910C200 830 400 820 600 850C800 880 1000 870 1200 800V812C1000 882 800 890 600 862C400 836 200 850 0 935Z" fill="url(#band)"/>
  </svg>

  <svg class="wave" style="top:2860px" width="1200" height="470" viewBox="0 0 1200 470">
    <path d="M0 0H1200V380C1000 320 800 330 600 400C400 470 200 440 0 390Z" fill="#f4f7fc"/>
    <path d="M0 390C200 450 400 470 600 410C800 350 1000 320 1200 400V430C1000 350 800 380 610 430C400 486 200 468 0 398Z" fill="url(#bandR)"/>
  </svg>

  <svg class="wave" style="top:3780px" width="1200" height="150" viewBox="0 0 1200 150">
    <path d="M0 70C200 20 400 10 620 70C820 124 1000 120 1200 80V88C1000 132 820 140 600 86C400 36 200 40 0 100Z" fill="url(#band)"/>
  </svg>

  <svg class="wave" style="top:4215px" width="1200" height="454" viewBox="0 0 1200 454">
    <path d="M0 90C220 20 420 10 620 60C820 110 1000 130 1200 70V454H0Z" fill="#f2f6fc"/>
    <path d="M0 96C220 20 420 14 620 64C820 114 1000 120 1200 46V80C1000 150 820 140 600 92C420 52 220 50 0 104Z" fill="url(#band)"/>
  </svg>

  <!-- header -->
  <div class="brand" style="left:136px;top:36px"><span class="brand-dot"></span>Bright Ledger View</div>
  <nav class="nav">
    <a class="active" href="#" style="left:506px">HOME</a>
    <a href="#" style="left:585px">ABOUT US</a>
    <a href="#" style="left:692px">ARTICLES</a>
    <a href="#" style="left:796px">CONTACT US</a>
  </nav>
  <div class="login">LOGIN</div>

  <!-- hero -->
  <h1 class="abs hero-title">Check your credit<br>score within seconds</h1>
  <p class="abs hero-sub">Lorem ipsum dolor sit amet, consectetur adipiscing elit,<br>sed do eiusmod tempor.</p>

  <div class="abs form-card">
    <h2 class="form-title">Get started now</h2>
    <div class="field" style="top:85px">Id number</div>
    <div class="field" style="top:138px">First name</div>
    <div class="field" style="top:188px">Last Name</div>
    <div class="field" style="top:239px">Email</div>
    <div class="field" style="top:292px">Mobile</div>
    <div class="agree"><i></i>I agree with the terms and conditions</div>
    <div class="btn-green">CHECK NOW</div>
  </div>

  <svg class="abs" style="left:380px;top:385px" width="380" height="410" viewBox="0 0 380 410">
    <path d="M10 5C60 60 110 90 130 160C150 250 200 300 300 310C360 318 370 360 345 395" fill="none" stroke="#222" stroke-width="1.5" stroke-dasharray="4 4"/>
    <path d="M336 385L345 398L356 389" fill="none" stroke="#222" stroke-width="1.5"/>
  </svg>

  <!-- about -->
  <div class="abs" style="left:139px;top:710px;width:472px;height:472px;border-radius:50%;background:var(--green)"></div>
  <div class="abs ph" role="img" aria-label="Photo of a hand using a calculator over financial papers" style="left:96px;top:678px;width:162px;height:162px;border-radius:50%;border:6px solid #fff;box-shadow:0 4px 14px rgba(0,0,0,.15)"></div>
  <div class="abs" role="img" aria-label="Product image: a sample credit report with a score gauge shown on a desktop screen and a tablet" style="left:170px;top:860px;width:430px;height:350px;border-radius:14px;background:linear-gradient(160deg,#e9eef5,#b9c6d6)"></div>

  <h2 class="abs about-title">ABOUT US</h2>
  <p class="abs about-text"><b>Lorem ipsum dolor sit amet, consectetur adipiscing elit, sed do eiusmod tempor.</b><br>Lorem ipsum dolor sit amet, consectetur adipiscing elit, sed do eiusmod tempor.Lorem ipsum dolor sit amet, consectetur adipiscing elit, sed do eiusmod tempor.Lorem ipsum dolor sit amet, consectetur adipiscing elit, sed do eiusmod tempor.Lorem ipsum dolor sit amet, consectetur adipiscing elit, sed do eiusmod tempor.</p>
  <div class="btn-blue">LEARN MORE</div>

  <!-- system features -->
  <h2 class="h2" style="top:1422px">System Features</h2>
  <p class="abs feat-desc">Lorem ipsum dolor sit amet, consectetur adipiscing elit, sed do eiusmod<br>tempor. Lorem ipsum dolor sit amet, consectetur adipiscing elit, sed do eius-<br>mod tempor.</p>

  <div class="abs" role="img" aria-label="Illustration of people reviewing a credit score clipboard with a gauge and a report card" style="left:405px;top:1700px;width:410px;height:275px;border-radius:30px;background:linear-gradient(135deg,#d6e3f7,#aac6ee)"></div>

  <div class="feat" style="left:495px;top:1622px;width:220px">Improve your credit<br>score eBook</div>
  <div class="feat" style="left:745px;top:1666px;width:240px">Personal Budgeting<br>Spreadsheet</div>
  <div class="feat" style="left:128px;top:1675px;width:250px">Dispute generator -<br>easily manage disputes</div>
  <div class="feat" style="left:800px;top:1786px;width:230px">Perfect score video<br>course</div>
  <div class="feat" style="left:150px;top:1850px;width:220px">Budget tool - easily<br>create&nbsp; budget</div>
  <div class="feat" style="left:810px;top:1926px;width:225px">Personal Finance<br>Video Tutorials</div>
  <div class="feat" style="left:490px;top:2010px;width:270px">Dedicated 24/7 Support</div>

  <svg class="abs" style="left:0;top:1550px" width="1200" height="520" viewBox="0 0 1200 520" fill="none" stroke="#333" stroke-width="1.5" stroke-dasharray="4 4">
    <path d="M450 160C440 100 460 40 510 18C540 10 540 40 535 65"/>
    <path d="M400 235C370 260 310 250 280 190"/>
    <path d="M800 215C830 210 860 200 880 182"/>
    <path d="M820 340C870 345 910 330 935 292"/>
    <path d="M410 370C390 360 370 350 348 333"/>
    <path d="M790 440C815 510 890 525 910 460"/>
    <path d="M530 420C540 440 545 450 545 460"/>
  </svg>

  <!-- testimonials -->
  <h2 class="h2" style="top:2262px">Testimonials</h2>

  <svg class="arrow" style="left:70px" viewBox="0 0 26 26"><path d="M22 13H5M12 5L4 13L12 21" fill="none" stroke="var(--blue)" stroke-width="3.5"/></svg>
  <svg class="arrow" style="left:1104px" viewBox="0 0 26 26"><path d="M4 13H21M14 5L22 13L14 21" fill="none" stroke="var(--blue)" stroke-width="3.5"/></svg>

  <article class="tcard" style="left:120px">
    <div class="quote">&#8220;</div>
    <div class="meta"><span class="stars">★★★★★</span><span class="date">Sep 09</span></div>
    <p>Lorem Ipsum is simply dummy text of the printing and typesetting industry. Lorem Ipsum has been the industry's standard dummy text ever since the 1500s..</p>
    <div class="name">Peter M.</div>
    <div class="role">CEO, Summit Holdings</div>
  </article>
  <article class="tcard" style="left:613px">
    <div class="quote">&#8220;</div>
    <div class="meta"><span class="stars">★★★★★</span><span class="date">Sep 09</span></div>
    <p>Lorem Ipsum is simply dummy text of the printing and typesetting industry. Lorem Ipsum has been the industry's standard dummy text ever since the 1500s..</p>
    <div class="name">Peter M.</div>
    <div class="role">CEO, Summit Holdings</div>
    <div class="abs" style="right:-40px;bottom:-40px;width:110px;height:110px;border-radius:50%;background:#d7e4f5"></div>
  </article>
  <div class="avatar ph" role="img" aria-label="Customer portrait" style="left:142px;top:2347px;width:60px;height:60px"></div>
  <div class="avatar ph" role="img" aria-label="Customer portrait" style="left:636px;top:2347px;width:60px;height:60px"></div>

  <!-- google reviews -->
  <h2 class="h2" style="top:2750px">Google Reviews</h2>

  <article class="rcard" style="left:160px;top:2951px;height:272px">
    <div class="avatar ph" role="img" aria-label="Reviewer portrait"></div>
    <h3>Thandi Mokoena</h3>
    <p>The credit report is easy to use, in-formative and accurate to the date. Helps me to manage my financial well-being.</p>
    <div class="stars">★★★★★</div>
  </article>
  <article class="rcard" style="left:457px;top:2897px;height:276px">
    <div class="avatar ph" role="img" aria-label="Reviewer portrait"></div>
    <h3>Carla Jansen</h3>
    <p>Their customer support team has been very impressive. The tools and knowledge they shared were of great practical use.</p>
    <div class="stars">★★★★★</div>
  </article>
  <article class="rcard" style="left:752px;top:2846px;height:276px">
    <div class="avatar ph" role="img" aria-label="Reviewer portrait"></div>
    <h3>Iron Crest ZA</h3>
    <p>Excellent credit report service. They respond to queries promptly, and have a very detailed credit report which is helpful and informative</p>
    <div class="stars">★★★★★</div>
  </article>

  <!-- why us -->
  <h2 class="h2" style="top:3366px;font-size:28px">Why get your score from us?</h2>
  <div class="acc" style="top:3459px;height:64px"><span class="q">We don't abuse your personal information:</span><span class="pm">+</span></div>
  <div class="acc" style="top:3526px;height:64px"><span class="q">Our report is super easy to understand:</span><span class="pm">+</span></div>
  <div class="acc open" style="top:3593px;height:150px"><span class="q">300,000 + South Africans have trusted us:</span><span class="pm">&minus;</span>
    <p class="a">Since 2008 we have helped over 300,000 South Africans make sense of their credit reports, so you can rest assured knowing that we have a proven track record and that you are in safe hands with us.</p>
  </div>

  <!-- payments -->
  <div class="pay" style="left:133px">Meridian Card</div>
  <div class="pay blue" style="left:378px">Cobalt Pay</div>
  <div class="pay" style="left:622px">Orbit Pay</div>
  <div class="pay blue" style="left:867px">Vantix</div>

  <!-- footer -->
  <div class="brand" style="left:136px;top:4420px"><span class="brand-dot"></span>Bright Ledger View</div>
  <div class="social" role="img" aria-label="Social profile link" style="left:130px"></div>
  <div class="social" role="img" aria-label="Social profile link" style="left:175px"></div>
  <div class="social" role="img" aria-label="Social profile link" style="left:222px"></div>
  <div class="social" role="img" aria-label="Social profile link" style="left:270px"></div>

  <div class="fcol" style="left:399px">
    <h4>Navigation</h4>
    <ul><li>Home</li><li>About us</li><li>Articles</li><li>Contact us</li></ul>
  </div>
  <div class="fcol" style="left:638px">
    <h4 class="sm">Resources</h4>
    <ul><li>Terms &amp; Conditions</li><li>Prvacy Policy</li></ul>
  </div>
  <div class="fcol" style="left:847px;padding-left:24px">
    <h4 class="sm">Contact Information</h4>
  </div>
  <div class="cinfo" style="top:4430px">
    <span class="ic"><svg width="14" height="16" viewBox="0 0 14 16"><path d="M7 15C7 15 1.5 9.5 1.5 6A5.5 5.5 0 0 1 12.5 6C12.5 9.5 7 15 7 15Z" fill="#fff"/><circle cx="7" cy="6" r="2" fill="var(--green)"/></svg></span>
    <span>78 MERIDIAN AVE - B- BLOCK,<br>CAPE TOWN, WC 8001</span>
  </div>
  <div class="cinfo" style="top:4472px">
    <span class="ic"><svg width="14" height="14" viewBox="0 0 14 14"><path d="M3 1L5.5 4L4.2 5.6C5 7.3 6.7 9 8.4 9.8L10 8.5L13 11L11.5 13C6 12.5 1.5 8 1 2.5Z" fill="#fff"/></svg></span>
    <span>+123 555 0142</span>
  </div>
  <div class="cinfo" style="top:4516px">
    <span class="ic"><svg width="15" height="11" viewBox="0 0 15 11"><rect x="0.5" y="0.5" width="14" height="10" rx="1" fill="#fff"/><path d="M1 1L7.5 6L14 1" fill="none" stroke="var(--green)" stroke-width="1.2"/></svg></span>
    <span>INFO@BRIGHTLEDGERVIEW.CO.ZA</span>
  </div>

  <div class="abs" style="left:0;top:4611px;width:1200px;height:1px;background:var(--line)"></div>
  <p class="copy">© 2022 BRIGHTLEDGERVIEW ALL RIGHT RESERVED</p>
</div>
</body>
</html>
```